Pebble Grocer

Hope all is well!

Wanted to make business cards for my father. His name is Samir Haddad and owns convenience stores. I have attached logo :)

He does not want any title just simple name and phone. An email would be nice as well.

Samir Haddad
Cell: 413-555-0148
Store: 413-555-0192

Pebblegrocer518@mailnest.example

The design and style is totally up to you :) The colors we were looking for were the same as logo :)

```html
<!DOCTYPE html>
<html lang="en">
<head>
<meta charset="utf-8">
<title>Pebble Grocer — Business Card</title>
<link href="https://fonts.googleapis.com/css2?family=Libre+Baskerville:wght@400;700&display=swap" rel="stylesheet">
<style>
  :root {
    --navy: #243b7d;
    --red: #e8313d;
    --paper: #ffffff;
    --backdrop: #a7a8ac;
    --shadow: rgba(0, 0, 0, 0.35);
  }
  * { margin: 0; padding: 0; box-sizing: border-box; }
  html, body {
    width: 697px;
    height: 1200px;
    overflow: hidden;
    background: var(--backdrop);
    font-family: "Libre Baskerville", Georgia, serif;
  }
  .canvas {
    position: relative;
    width: 697px;
    height: 1200px;
  }
  .card {
    position: absolute;
    width: 423px;
    height: 246px;
    background: var(--paper);
    box-shadow: 6px 8px 10px var(--shadow);
    overflow: hidden;
  }
  .card--front { left: 65px; top: 330px; }
  .card--back  { left: 214px; top: 660px; }

  .brand {
    position: absolute;
    display: flex;
    align-items: center;
    gap: 8px;
    color: var(--navy);
    font-weight: 700;
    font-size: 25px;
    letter-spacing: 0.5px;
    white-space: nowrap;
  }
  .brand__dot {
    width: 14px;
    height: 14px;
    border-radius: 50%;
    background: var(--red);
    flex: none;
  }
  .card--front .brand { left: 50%; top: 40px; transform: translateX(-50%); }
  .card--back .brand  { left: 50%; top: 50%; transform: translate(-50%, -50%); }

  .holder-name {
    position: absolute;
    left: 39px;
    top: 106px;
    color: var(--navy);
    font-weight: 700;
    font-size: 20px;
  }
  .contacts {
    position: absolute;
    left: 35px;
    top: 142px;
    list-style: none;
  }
  .contacts__item {
    display: flex;
    align-items: center;
    gap: 6px;
    height: 20px;
    color: var(--navy);
    font-weight: 700;
    font-size: 11.5px;
  }
  .contacts__item svg { width: 13px; height: 13px; flex: none; }
  .contacts__label {
    color: var(--red);
    font-weight: 400;
    font-size: 10.5px;
    margin-left: 2px;
  }

  .stripes {
    position: absolute;
    left: 0;
    top: 207px;
    width: 290px;
    height: 29px;
    background: repeating-linear-gradient(
      to bottom,
      var(--red) 0 5px,
      var(--paper) 5px 11px
    );
  }
  .red-block {
    position: absolute;
    left: 297px;
    top: 207px;
    width: 126px;
    height: 29px;
    background: var(--red);
  }
</style>
</head>
<body>
<main class="canvas">

  <section class="card card--front" aria-label="Business card front">
    <div class="brand"><span class="brand__dot"></span>Pebble Grocer</div>

    <h1 class="holder-name">Samir Haddad</h1>

    <ul class="contacts">
      <li class="contacts__item">
        <svg viewBox="0 0 20 20" aria-hidden="true"><circle cx="10" cy="10" r="10" fill="var(--red)"/><path d="M7 5.5c.6-.4 1.2-.2 1.5.4l.8 1.6c.2.5 0 1-.4 1.3l-.6.4c.5 1.2 1.4 2.1 2.5 2.6l.4-.6c.3-.4.8-.6 1.3-.4l1.6.8c.6.3.8.9.4 1.5l-.6.8c-.5.7-1.4.9-2.2.6-2.7-1-4.7-3-5.7-5.7-.3-.8-.1-1.7.6-2.2z" fill="#fff"/></svg>
        413-555-0148
      </li>
      <li class="contacts__item">
        <svg viewBox="0 0 20 20" aria-hidden="true"><circle cx="10" cy="10" r="10" fill="var(--red)"/><path d="M7 5.5c.6-.4 1.2-.2 1.5.4l.8 1.6c.2.5 0 1-.4 1.3l-.6.4c.5 1.2 1.4 2.1 2.5 2.6l.4-.6c.3-.4.8-.6 1.3-.4l1.6.8c.6.3.8.9.4 1.5l-.6.8c-.5.7-1.4.9-2.2.6-2.7-1-4.7-3-5.7-5.7-.3-.8-.1-1.7.6-2.2z" fill="#fff"/></svg>
        413-555-0192<span class="contacts__label">(Store)</span>
      </li>
      <li class="contacts__item">
        <svg viewBox="0 0 20 20" aria-hidden="true"><circle cx="10" cy="10" r="10" fill="var(--red)"/><rect x="5" y="6.5" width="10" height="7" rx="1" fill="#fff"/><path d="M5.5 7l4.5 3.6L14.5 7" fill="none" stroke="var(--red)" stroke-width="1"/></svg>
        Pebblegrocer518@mailnest.example
      </li>
    </ul>

    <div class="stripes"></div>
    <div class="red-block"></div>
  </section>

  <section class="card card--back" aria-label="Business card back">
    <div class="brand"><span class="brand__dot"></span>Pebble Grocer</div>
  </section>

</main>
</body>
</html>
```